For our annual dance recital this year we will have an asylum/ orphans/ any spooky shelter. Thats the feel of it.
i will be need an invitation and a ticket.
as the recital will be done in two days the tickets will have same design but different colors.
My idea is to have spooky fonts/ x ray images somehow put in the design.
i will be uploading a lot of images for you to understand where i would like to take this design.
for the invitation i do want to have part of the paper printed in see through material like some of the images uploaded or have an x-ray effect.
the invitation should have this written on it.
DUSKMORE
Our production is ready and we are dying to have you around. So crawl on over for a spooktacular happening at
QASR MIRWAN UNIVERSITY AUDITORIUM
The undertaking will begin from 1:30pm to 3:30pm
May 2nd 2014 and May 3rd 2014
The entry tickets will be two colors but same design. i would like it to be printed of see through plastic paper. so we can have one see through and font in black and the other one is dark see through written in white maybe. please make in an xray effext with maybe the pointed feet picture somehow incorporated in the design
i want it to look like the picture i uploaded of (Wendels 4th birthday) in regard of layout of the writings i like how the date is stamped and i like how the date is pointed out in a dot.
here what to write on tickets
The name of the recital
Issued by Pavrella
DUSKMORE
(Find me a sentence that means admit one)
we do need numbers as the seats are numbered
so all in all i would like the invitation and ticket to go together i was thinking of having the dancer bridge xray on invitation and the pointed feet on the ticket.
if you have any other nice parts of the body xray that somehow show its a dancer im also open to that.
than main idea is to have a nice design that is so creative yet simple. play with the fonts to deliver this spooky feeling but all with elegance.
please notice that the picture with the person smoking Xray .. i like how its black and the words are see through with the xray picture. so this would be nice as an idea.
Reason: I still did not find a design that i like.
the theme is asylum. i want it creepy but in the same time ELEGANT. I will be printing invitation on CLEAR paper so the X ray picture could be incorporated in the design in a very subtle way.
Please ask me any question if its not clear
PS my budget is higher now.

```html
<!DOCTYPE html>
<html lang="en">
<head>
<meta charset="utf-8">
<title>DUSKMORE – Invitation</title>
<link rel="stylesheet" href="https://fonts.googleapis.com/css2?family=Metal+Mania&family=Montserrat:wght@400;500;700&display=swap">
<style>
  :root {
    --page: #ffffff;
    --card: #050505;
    --card-edge: #3a3a3a;
    --glow: #f2e21a;
    --glow-soft: #8d8410;
    --bone: #f4f4f0;
    --ink-light: #ffffff;
  }
  * { box-sizing: border-box; margin: 0; padding: 0; }
  html, body {
    width: 1200px; height: 726px; overflow: hidden;
    background: var(--page);
    font-family: "Montserrat", Arial, sans-serif;
  }
  .invitation {
    position: absolute; left: 100px; top: 128px;
    width: 1000px; height: 470px;
    background:
      radial-gradient(ellipse at 50% 50%, var(--card) 72%, var(--card-edge) 100%);
    overflow: hidden;
  }
  .xray-dancer {
    position: absolute; left: 40px; top: 40px;
    width: 310px; height: 400px;
    background:
      radial-gradient(ellipse 45% 40% at 45% 55%, rgba(242,226,26,.85), rgba(141,132,16,.35) 60%, transparent 80%),
      radial-gradient(ellipse 30% 25% at 70% 20%, rgba(244,244,240,.5), transparent 75%);
    border-radius: 40px;
  }
  .title {
    position: absolute; left: 330px; top: 28px;
    font-family: "Metal Mania", "Creepster", cursive;
    font-size: 104px; letter-spacing: 8px; line-height: 1;
    color: var(--glow);
  }
  .title .fade { color: var(--ink-light); }
  .message {
    position: absolute; left: 336px; top: 158px; width: 620px;
    font-size: 18.5px; line-height: 1.22; font-weight: 500;
    background: linear-gradient(90deg, var(--glow) 0 55%, var(--ink-light) 80%);
    -webkit-background-clip: text; background-clip: text;
    color: transparent;
  }
  .venue { text-transform: uppercase; }
  .calendar { position: absolute; left: 0; top: 0; }
  .months {
    position: absolute; display: flex; align-items: flex-end;
  }
  .months--past { left: 400px; top: 292px; color: var(--glow); align-items: flex-end; height: 80px; }
  .months--ahead { left: 590px; top: 226px; color: var(--ink-light); align-items: flex-start; height: 80px; }
  .cell {
    border: 2px solid currentColor; margin-left: -2px;
    display: flex; align-items: center; justify-content: center;
    font-weight: 700;
  }
  .cell--month {
    width: 32px; height: 80px;
    writing-mode: vertical-rl; transform: rotate(180deg);
    font-size: 15px; letter-spacing: 1px; position: relative;
  }
  .cell--year { width: 42px; height: 38px; font-size: 16px; }
  .dot {
    position: absolute; width: 16px; height: 16px; border-radius: 50%;
    background: var(--glow); left: 6px; top: 4px;
  }
  .days {
    position: absolute; left: 398px; top: 386px;
    font-size: 12.5px; font-weight: 700; letter-spacing: .5px;
    display: flex; gap: 5px; align-items: center;
  }
  .days .past { color: var(--glow); }
  .days .ahead { color: var(--ink-light); }
  .days .marked {
    display: inline-block; width: 11px; height: 11px; border-radius: 50%;
    background: var(--glow);
  }
  .timing {
    position: absolute; left: 440px; top: 412px;
    font-size: 15px; font-weight: 700; color: var(--glow);
  }
</style>
</head>
<body>
  <article class="invitation">
    <div class="xray-dancer" role="img" aria-label="Glowing yellow X-ray of a dancer's skeleton arched in a back bridge"></div>

    <h1 class="title">DUSKMO<span class="fade">RE</span></h1>

    <p class="message">Our production is ready and we are dying to have you around. So crawl on over for a spooktacular happening at<br><span class="venue">Qasr Mirwan University Auditorium</span></p>

    <div class="calendar">
      <div class="months months--past">
        <div class="cell cell--year">20</div>
        <div class="cell cell--month">JAN</div>
        <div class="cell cell--month">FEB</div>
        <div class="cell cell--month">MAR</div>
        <div class="cell cell--month">APR</div>
        <div class="cell cell--month">MAY<span class="dot"></span></div>
      </div>
      <div class="months months--ahead">
        <div class="cell cell--month">JUN</div>
        <div class="cell cell--month">AUG</div>
        <div class="cell cell--month">SEP</div>
        <div class="cell cell--month">OCT</div>
        <div class="cell cell--month">NOV</div>
        <div class="cell cell--month">DEC</div>
        <div class="cell cell--year">14</div>
      </div>
      <div class="days">
        <span class="past">1</span><span class="marked"></span><span class="marked"></span>
        <span class="past">4</span><span class="past">5</span><span class="past">6</span><span class="past">7</span><span class="past">8</span><span class="past">9</span><span class="past">10</span><span class="past">11</span><span class="past">12</span><span class="past">13</span><span class="past">14</span><span class="past">15</span><span class="past">16</span>
        <span class="ahead">17</span><span class="ahead">18</span><span class="ahead">19</span><span class="ahead">20</span><span class="ahead">21</span><span class="ahead">22</span><span class="ahead">23</span><span class="ahead">24</span><span class="ahead">25</span><span class="ahead">26</span><span class="ahead">27</span><span class="ahead">28</span><span class="ahead">29</span><span class="ahead">30</span><span class="ahead">31</span>
      </div>
    </div>

    <p class="timing">The undertaking will begin from 1:30pm to 3:30pm</p>
  </article>
</body>
</html>
```